Management consultant needs business cards

We need a design for a personal/professional business card for a management consultant. Work is typically focused on the b2b space, helping companies improve their operations. The final design should communicate efficiency and helping companies and people achieve their full potential.

Company name is "Ashcombe Consultants"

Brand promise is "Spotting Strength - Accelerating Outcomes"

We come from major consulting firms (Haldrick, Tove, JNP) but would like to project a slightly more modern feel than those players.

Target Market(s)

Targeting B2B markets such as banks or companies.

Industry/Entity Type

Business

Requirements
Must have
• The card must communicate the following information:

Neil T Marbury
Managing Director
Ashcombe Consultants
Phone: 416-782-4051
neil.marbury@ashcombeconsultants.example
www.ashcombeconsultants.example

42 Pellmore Ave
Toronto, ON M6R 2J8

Back side should have
"Spotting Strength - Accelerating Outcomes"

```html
<!DOCTYPE html>
<html lang="en">
<head>
<meta charset="utf-8">
<title>Ashcombe Consultants — Business Card</title>
<link href="https://fonts.googleapis.com/css2?family=Raleway:wght@300;400;600&display=swap" rel="stylesheet">
<style>
  :root {
    --backdrop: #e4e4e2;
    --paper: #f7f7f5;
    --slate: #6a6a6a;
    --ink: #161616;
    --band: #0c0c0c;
    --mist: #ececec;
    --shadow: rgba(0, 0, 0, 0.18);
  }
  * { margin: 0; padding: 0; box-sizing: border-box; }
  html, body {
    width: 1200px;
    height: 1200px;
    overflow: hidden;
    background: var(--backdrop);
    font-family: "Raleway", "Helvetica Neue", Arial, sans-serif;
  }
  .canvas {
    width: 1200px;
    height: 1200px;
    display: flex;
    flex-direction: column;
    align-items: center;
    justify-content: center;
    gap: 60px;
  }
  .card {
    position: relative;
    width: 840px;
    height: 480px;
    background: var(--paper);
    box-shadow: 0 10px 30px var(--shadow);
    overflow: hidden;
    color: var(--ink);
    text-transform: uppercase;
    text-align: center;
  }

  /* Contact side */
  .card-header {
    position: absolute;
    inset: 0 0 auto 0;
    height: 150px;
    background: var(--slate);
  }
  .card-header svg { position: absolute; inset: 0; }
  .company-name {
    position: absolute;
    inset: 22px 0 auto 0;
    font-weight: 300;
    font-size: 44px;
    line-height: 52px;
    letter-spacing: 0.3em;
    padding-left: 0.3em;
    color: var(--mist);
  }
  .contact {
    position: absolute;
    top: 168px;
    left: 0;
    right: 0;
  }
  .person-name {
    font-weight: 400;
    font-size: 28px;
    letter-spacing: 0.18em;
  }
  .person-title {
    font-weight: 600;
    font-size: 11px;
    letter-spacing: 0.12em;
    margin-top: 2px;
  }
  .phone {
    font-weight: 400;
    font-size: 26px;
    letter-spacing: 0.16em;
    margin-top: 12px;
  }
  .email {
    font-weight: 400;
    font-size: 15px;
    letter-spacing: 0.14em;
    margin-top: 8px;
  }
  .address {
    font-weight: 400;
    font-size: 14px;
    letter-spacing: 0.18em;
    line-height: 20px;
    margin-top: 10px;
  }
  .web-band {
    position: absolute;
    inset: auto 0 0 0;
    height: 78px;
    background: var(--band);
    color: var(--mist);
    font-weight: 400;
    font-size: 22px;
    letter-spacing: 0.24em;
    line-height: 78px;
  }

  /* Promise side */
  .promise {
    position: absolute;
    top: 80px;
    left: 0;
    right: 0;
    font-weight: 300;
    letter-spacing: 0.28em;
  }
  .promise-line { font-size: 36px; line-height: 48px; }
  .promise-dash { font-size: 30px; line-height: 44px; }
  .peak-band { position: absolute; inset: 0; }
  .peak-name {
    font-family: "Raleway", "Helvetica Neue", Arial, sans-serif;
    font-weight: 400;
    font-size: 15px;
    letter-spacing: 0.25em;
    fill: var(--mist);
  }
</style>
</head>
<body>
<main class="canvas">

  <section class="card card-contact" aria-label="Business card, contact side">
    <header class="card-header">
      <svg width="840" height="150" viewBox="0 0 840 150" aria-hidden="true">
        <line x1="0" y1="30" x2="72" y2="150" stroke="#dcdcdc" stroke-width="1.5"/>
        <line x1="840" y1="30" x2="768" y2="150" stroke="#dcdcdc" stroke-width="1.5"/>
      </svg>
      <h1 class="company-name">Ashcombe<br>Consultants</h1>
    </header>

    <div class="contact">
      <p class="person-name">Neil T Marbury</p>
      <p class="person-title">Managing Director</p>
      <p class="phone">416-782-4051</p>
      <p class="email">neil.marbury@ashcombeconsultants.example</p>
      <p class="address">42 Pellmore Ave<br>Toronto, ON M6R 2J8</p>
    </div>

    <footer class="web-band">www.ashcombeconsultants.example</footer>
  </section>

  <section class="card card-promise" aria-label="Business card, brand promise side">
    <div class="promise">
      <p class="promise-line">Spotting Strength</p>
      <p class="promise-dash">-</p>
      <p class="promise-line">Accelerating Outcomes</p>
    </div>

    <svg class="peak-band" width="840" height="480" viewBox="0 0 840 480" aria-hidden="true">
      <polygon points="0,380 315,380 420,285 525,380 840,380 840,462 0,462" fill="#0c0c0c"/>
      <text class="peak-name" x="422" y="366" text-anchor="middle">ASHCOMBE</text>
    </svg>
  </section>

</main>
</body>
</html>
```